brindlewood carpentry business card 2.0

id like to get some extra info added to my current business card ,but i am also open to a new design as well ,id like it to be a clean professional look
i have attached the original card files, i have also attached the ridgemark guild logo and licensed builder logo that id like to add to all the current info on the old card
also the color green is important as seen in the company logo

Industry/Entity Type

Carpentry

Colors
9bcb3c

```html
<!DOCTYPE html>
<html lang="en">
<head>
<meta charset="UTF-8">
<title>Brindlewood Carpentry – Business Card</title>
<link href="https://fonts.googleapis.com/css2?family=Lato:wght@400;700&display=swap" rel="stylesheet">
<style>
  :root {
    --brand-green: #9bcb3c;
    --card-black: #0b0b0b;
    --card-white: #f7f7f7;
    --ink: #1a1a1a;
    --text-light: #ffffff;
    --badge-blue: #1c3f8f;
    --badge-cream: #f2f2f2;
    --backdrop: #e6e6e6;
  }
  html, body {
    margin: 0;
    padding: 0;
    width: 1200px;
    height: 900px;
    overflow: hidden;
    background: var(--backdrop);
    font-family: "Lato", Arial, sans-serif;
  }
  .canvas {
    position: relative;
    width: 1200px;
    height: 900px;
  }
  .business-card {
    position: absolute;
    left: 80px;
    top: 127px;
    width: 1040px;
    height: 646px;
    background: var(--card-black);
    box-shadow: 0 10px 30px rgba(0,0,0,0.18);
    overflow: hidden;
  }
  .card-top {
    position: absolute;
    left: 0; top: 0;
    width: 100%;
    height: 315px;
    background: var(--card-white);
  }
  .wordmark {
    position: absolute;
    left: 0; right: 0;
    top: 92px;
    text-align: center;
    color: var(--ink);
    font-weight: 400;
    line-height: 1;
  }
  .wordmark-name {
    display: block;
    font-size: 84px;
    letter-spacing: 3px;
  }
  .wordmark-sub {
    display: block;
    margin-top: 14px;
    margin-left: 300px;
    font-size: 40px;
    letter-spacing: 2px;
  }
  .accent-rule {
    position: absolute;
    left: 0; top: 315px;
    width: 100%;
    height: 10px;
    background: var(--brand-green);
  }
  .contact-block {
    position: absolute;
    left: 70px;
    top: 378px;
    color: var(--text-light);
  }
  .person-name {
    margin: 0;
    font-size: 36px;
    font-weight: 700;
    color: var(--brand-green);
    letter-spacing: 0.5px;
  }
  .person-role {
    margin: 4px 0 0;
    font-size: 28px;
    font-weight: 400;
  }
  .contact-list {
    list-style: none;
    margin: 40px 0 0;
    padding: 0;
  }
  .contact-item {
    display: flex;
    align-items: center;
    font-size: 27px;
    line-height: 38px;
  }
  .contact-icon {
    width: 30px;
    height: 30px;
    margin-right: 12px;
    flex: none;
  }
  .badge-guild {
    position: absolute;
    left: 659px;
    top: 450px;
    width: 122px;
    height: 144px;
    background: var(--badge-cream);
    box-sizing: border-box;
    border: 6px solid var(--badge-cream);
  }
  .badge-guild-inner {
    width: 100%;
    height: 74%;
    background: var(--badge-blue);
  }
  .badge-licence {
    position: absolute;
    left: 821px;
    top: 446px;
    width: 160px;
    height: 160px;
    border-radius: 50%;
    background: var(--brand-green);
    box-sizing: border-box;
    border: 8px solid var(--badge-cream);
  }
</style>
</head>
<body>
<main class="canvas">
  <section class="business-card">
    <div class="card-top">
      <div class="wordmark">
        <span class="wordmark-name">BRINDLEWOOD</span>
        <span class="wordmark-sub">CARPENTRY</span>
      </div>
    </div>
    <div class="accent-rule"></div>

    <div class="contact-block">
      <h1 class="person-name">DANIEL HARLOW</h1>
      <p class="person-role">Director / Brindlewood Carpentry Ltd</p>
      <ul class="contact-list">
        <li class="contact-item">
          <svg class="contact-icon" viewBox="0 0 30 30" aria-hidden="true">
            <rect x="2" y="2" width="26" height="26" rx="4" fill="none" stroke="var(--brand-green)" stroke-width="2.5"/>
            <path d="M10 8 l3 0 l1.5 4 l-2 1.5 q1.5 3.5 4.5 4.5 l1.5 -2 l4 1.5 l0 3 q-8 1 -12.5 -12.5 z" fill="var(--brand-green)"/>
          </svg>
          02109481536
        </li>
        <li class="contact-item">
          <svg class="contact-icon" viewBox="0 0 30 30" aria-hidden="true">
            <rect x="2" y="6" width="26" height="18" fill="var(--brand-green)"/>
            <path d="M2 6 l13 10 l13 -10" fill="none" stroke="var(--card-black)" stroke-width="2"/>
          </svg>
          daniel@brindlewoodcarpentry.co.nz
        </li>
        <li class="contact-item">
          <svg class="contact-icon" viewBox="0 0 30 30" aria-hidden="true">
            <g fill="none" stroke="var(--brand-green)" stroke-width="2.5">
              <circle cx="15" cy="15" r="12"/>
              <ellipse cx="15" cy="15" rx="5" ry="12"/>
              <line x1="3" y1="15" x2="27" y2="15"/>
              <path d="M5 9 h20 M5 21 h20"/>
            </g>
          </svg>
          www.brindlewoodcarpentry.co.nz
        </li>
      </ul>
    </div>

    <div class="badge-guild" role="img" aria-label="Ridgemark Guild registered member badge">
      <div class="badge-guild-inner"></div>
    </div>
    <div class="badge-licence" role="img" aria-label="Licensed builder certification badge"></div>
  </section>
</main>
</body>
</html>
```